Cover graphic for law firm brochure

We need cover art designed for a brochure which will also serve for our client’s design on social media banners. We would love a creative design that could incorporate the design elements from the circle in the logo or other design elements for a Washington, D.C.-based law firm that specializes in government contracting. Attached is their logo for colors and brand feel. The front page of the brochure needs to have their logo on it. A design element using their logo or the circle from their logo, would be great to see. The planes need to be removed. We would love to see options for the back but our client likes this image.

We would love to see abstract art creation using the colors from the logo, you can also do a pop of gold from the capital building.

The dimensions are 24x8. We will upload a high-resolution logo and the full brochure in the coming day or two.

If you are going to add text to the front please use this text: Holt & Crane is a boutique law firm built to provide exceptional representation to government contractors.

The other option is to do something grey scale with pops of colors with the DC Skyline, American Flags (with one in color), or other items. On the back of the cover, I would love to see a design option that carries through from the front. You can use elements from the capital building that is already there or other images.

Please do not reach out to the client directly as they are busy. Please only communicate through the platform.

We are excited to see your creative designs!
Updates

I will be sending out the high-res logo and brochure dimensions shortly.

Target Market(s)

areospace and defense industry

Industry/Entity Type

Legal

Font styles to use
Other font styles liked:
• See logo

Colors

Designer to choose colors to be used in the design.

Requirements
Must have
• If doing a graphic creation, use of colors from logo and abstract design that is conservative, upscale and elegant feeling. If doing a cover with an image a picture that is similar to the one below or something that is related.
Should not have
• Law related images of scales, gavels or other law items, please do not use an image of the capital on the front as that is the back image.

```html
<!DOCTYPE html>
<html lang="en">
<head>
<meta charset="utf-8">
<title>Holt &amp; Crane — Brochure Cover</title>
<link href="https://fonts.googleapis.com/css2?family=Cormorant+Garamond:wght@500&family=Tinos&display=swap" rel="stylesheet">
<style>
  :root{
    --backdrop:#d9d9da;
    --paper:#ffffff;
    --ring-outer:#ececed;
    --ring-inner:#f4f4f5;
    --navy:#4a5775;
    --navy-deep:#3a4764;
    --sky-light:#f0f0f1;
    --sky-mid:#b9bbbf;
    --sky-dark:#6c6e73;
    --band-text:#ffffff;
  }
  *{margin:0;padding:0;box-sizing:border-box}
  html,body{width:1200px;height:900px;overflow:hidden;background:var(--backdrop)}
  .cover{
    position:absolute;left:210px;top:60px;width:780px;height:780px;
    background:var(--paper);overflow:hidden;
    box-shadow:0 6px 24px rgba(0,0,0,.12);
  }
  .cover-art{position:absolute;inset:0;width:780px;height:780px}
  .brand{
    position:absolute;left:300px;top:150px;
    display:flex;align-items:center;gap:16px;
  }
  .brand-mark{
    width:64px;height:64px;border-radius:50%;background:var(--navy);flex:none;
  }
  .brand-name{
    font-family:"Cormorant Garamond",serif;font-weight:500;
    font-size:40px;letter-spacing:3px;color:var(--navy);text-transform:uppercase;
    line-height:1;
  }
  .tagline{
    position:absolute;left:170px;top:640px;width:520px;
    font-family:"Tinos",serif;font-size:24px;line-height:1.3;color:var(--band-text);
  }
</style>
</head>
<body>
  <main class="cover">
    <svg class="cover-art" viewBox="0 0 780 780" aria-hidden="false">
      <defs>
        <linearGradient id="skylineTone" x1="0" y1="0" x2="0" y2="1">
          <stop offset="0" stop-color="var(--sky-light)"/>
          <stop offset="0.45" stop-color="var(--sky-mid)"/>
          <stop offset="1" stop-color="var(--sky-dark)"/>
        </linearGradient>
        <clipPath id="innerCircle">
          <circle cx="440" cy="400" r="300"/>
        </clipPath>
      </defs>
      <circle class="ring-outer" cx="440" cy="400" r="360" fill="var(--ring-outer)"/>
      <circle class="ring-gap" cx="440" cy="400" r="322" fill="var(--paper)"/>
      <circle class="ring-inner" cx="440" cy="400" r="310" fill="var(--ring-inner)"/>
      <rect class="skyline-photo" role="img" aria-label="Greyscale city skyline photograph across a waterfront"
            x="120" y="250" width="660" height="380" fill="url(#skylineTone)" clip-path="url(#innerCircle)"/>
      <path class="navy-band" d="M0 600 Q380 520 780 470 L780 780 L0 780 Z" fill="var(--navy)"/>
    </svg>

    <div class="brand">
      <span class="brand-mark"></span>
      <span class="brand-name">Holt &amp; Crane</span>
    </div>

    <p class="tagline">Holt &amp; Crane is a boutique law firm built to provide exceptional representation to government contractors.</p>
  </main>
</body>
</html>
```